Gift Certificate style graphic that could be reused for mulitple giveaways

We are looking for a gift certificate/giveaway certificate design , so that we can change and write different giveaways on it over time.
We would like our colors to represent our brand, please refer to the website to see . www.marbletonkitchen.com . Ill attached some photos of our food, as well as our logo.

On the certificate , we would need these 3 items included at a minimum.
1.
CONGRATULATIONS!
YOU HAVE WON
____________________
2.
Stop by your nearest Marbleton Kitchen to redeem your prize.
Nearest location is : _______________________
3.
This certificate will expire on : _____________________

Make the design look exciting, and not boring. Use some colour throughout.

SIZE : 8 1/2 x 11 please

Industry/Entity Type

Restaurant

Requirements
Must have
• Logo, food pictures, and the 3 items discussed in brief
Nice to have
• colourful, eye catching

```html
<!DOCTYPE html>
<html lang="en">
<head>
<meta charset="utf-8">
<title>Marbleton Kitchen Gift Certificate</title>
<link rel="stylesheet" href="https://fonts.googleapis.com/css2?family=Luckiest+Guy&family=Titan+One&family=Gochi+Hand&family=Poppins:wght@400;500;600;700&display=block">
<style>
  :root {
    --page-bg: #e4e4e4;
    --card-light: #ffffff;
    --card-grey: #e6e6e6;
    --ink: #1e1e1e;
    --brand-green: #8cc43f;
    --brand-green-dark: #6aa52a;
    --rule: #9a9a9a;
    --salad-light: #b9d98a;
    --salad-dark: #5f9a2c;
  }
  html, body {
    margin: 0;
    width: 800px;
    height: 1200px;
    overflow: hidden;
    background: var(--page-bg);
  }
  .certificate {
    position: absolute;
    left: 30px;
    top: 428px;
    width: 740px;
    height: 343px;
    box-shadow: 0 6px 18px rgba(0,0,0,0.18);
  }
  .certificate svg { display: block; }
  .headline {
    font-family: "Luckiest Guy", "Titan One", "Arial Black", Impact, sans-serif;
    font-weight: 900;
    font-size: 62px;
    fill: var(--ink);
    stroke: var(--brand-green);
    stroke-width: 3px;
    stroke-linejoin: round;
    paint-order: stroke fill;
  }
  .subhead {
    font-family: "Gochi Hand", "Comic Sans MS", cursive;
    font-size: 38px;
    fill: var(--ink);
  }
  .instruction {
    font-family: "Poppins", Arial, sans-serif;
    font-weight: 700;
    font-size: 10.5px;
    fill: var(--ink);
  }
  .field-label {
    font-family: "Poppins", Arial, sans-serif;
    font-weight: 600;
    font-size: 10.5px;
    fill: var(--ink);
  }
  .fill-rule {
    stroke: var(--rule);
    stroke-width: 0.7;
  }
  .brand-name {
    font-family: "Poppins", Arial, sans-serif;
    font-weight: 700;
    font-size: 15px;
    fill: var(--brand-green-dark);
  }
  .website {
    font-family: "Poppins", Arial, sans-serif;
    font-weight: 400;
    font-size: 11.5px;
    fill: var(--ink);
  }
  .plate-arc {
    fill: none;
    stroke: var(--ink);
    stroke-width: 1;
    stroke-dasharray: 4 3;
  }
</style>
</head>
<body>
  <div class="certificate">
    <svg width="740" height="343" viewBox="0 0 740 343">
      <defs>
        <linearGradient id="card-surface" x1="0" y1="0" x2="1" y2="0.4">
          <stop offset="0" stop-color="var(--card-grey)"/>
          <stop offset="0.45" stop-color="var(--card-light)"/>
          <stop offset="1" stop-color="#f1f1f1"/>
        </linearGradient>
        <radialGradient id="salad-tone" cx="0.5" cy="0.45" r="0.6">
          <stop offset="0" stop-color="#d9b88a"/>
          <stop offset="0.35" stop-color="var(--salad-light)"/>
          <stop offset="1" stop-color="var(--salad-dark)"/>
        </radialGradient>
        <clipPath id="card-clip"><rect width="740" height="343"/></clipPath>
      </defs>

      <g clip-path="url(#card-clip)">
        <rect class="card-surface" width="740" height="343" fill="url(#card-surface)"/>

        <polygon class="green-splash" fill="var(--brand-green)"
          points="317,343 330,312 344,277 362,262 377,248 740,244 740,343"/>

        <path class="plate-arc" d="M449,139 Q600,72 740,148"/>

        <g class="salad-photo" role="img" aria-label="Grilled chicken Caesar salad in a white bowl">
          <ellipse cx="570" cy="222" rx="172" ry="110" fill="#f4f4f4"/>
          <ellipse cx="575" cy="216" rx="160" ry="96" fill="url(#salad-tone)"/>
        </g>
      </g>

      <text class="headline" x="34" y="86" textLength="640" lengthAdjust="spacingAndGlyphs">CONGRATULATIONS!</text>

      <text class="subhead" x="34" y="125" textLength="262" lengthAdjust="spacingAndGlyphs">YOU HAVE WON</text>
      <line class="fill-rule" x1="304" y1="124" x2="450" y2="124"/>

      <text class="instruction" x="33" y="169" textLength="354" lengthAdjust="spacingAndGlyphs">STOP BY YOUR NEAREST MARBLETON KITCHEN TO REDEEM YOUR PRIZE</text>

      <text class="field-label" x="33" y="187">Nearest location is :</text>
      <line class="fill-rule" x1="146" y1="184" x2="385" y2="184"/>
      <line class="fill-rule" x1="34" y1="203" x2="385" y2="203"/>

      <text class="field-label" x="34" y="228">This certificate will expire on :</text>
      <line class="fill-rule" x1="189" y1="225" x2="365" y2="225"/>

      <text class="brand-name" x="34" y="290" textLength="126" lengthAdjust="spacingAndGlyphs">Marbleton Kitchen</text>
      <text class="website" x="172" y="290" textLength="155" lengthAdjust="spacingAndGlyphs">www.marbletonkitchen.com</text>
    </svg>
  </div>
</body>
</html>
```